Adult Residential Care Provider (Assisted Living) needs a brochure design.

We need a brochure designed for our assisted living facilites in Metairie (adjacent to New Orleans) called Willowmere Elder Homes. We provide adults, typically Seniors, a place to live where they receive 24-hour care/support of their daily living activities, including laundering, cooking, cleaning, grooming, bathing, etc.. I'd like to use our logo and the color choices should be soft and convey comfort. I would also like the brochure to be editable by my administration to make any changes in the future.

```html
<!DOCTYPE html>
<html lang="en">
<head>
<meta charset="utf-8">
<title>Willowmere Elder Homes – Flyer</title>
<link href="https://fonts.googleapis.com/css2?family=Lora:wght@500;600&family=Cinzel:wght@500&family=Poppins:wght@400;600&display=swap" rel="stylesheet">
<style>
  :root {
    --page-bg: #ece9e6;
    --green-dark: #1f5b4d;
    --green: #2a6b5a;
    --cream: #f4ece0;
    --cream-light: #f7f2ea;
    --text: #1d2a26;
    --white: #ffffff;
  }
  * { margin: 0; padding: 0; box-sizing: border-box; }
  html, body { width: 1200px; height: 848px; overflow: hidden; }
  body {
    background: var(--page-bg);
    display: flex;
    align-items: center;
    justify-content: center;
    font-family: "Poppins", sans-serif;
  }
  .flyer {
    position: relative;
    width: 566px;
    height: 800px;
    background: linear-gradient(180deg, var(--cream-light) 0%, var(--cream) 100%);
    overflow: hidden;
    box-shadow: 4px 8px 18px rgba(0,0,0,0.25);
  }
  .hero-photo {
    position: absolute;
    left: 0; top: 0;
    width: 100%; height: 330px;
    background:
      radial-gradient(ellipse 60% 35% at 45% 62%, rgba(232,190,165,0.85), rgba(232,190,165,0) 70%),
      radial-gradient(ellipse 40% 50% at 85% 25%, rgba(176,214,170,0.7), rgba(176,214,170,0) 70%),
      radial-gradient(ellipse 40% 50% at 10% 20%, rgba(245,196,150,0.6), rgba(245,196,150,0) 70%),
      linear-gradient(180deg, #efe7ee 0%, #ece6e6 60%, var(--cream-light) 100%);
  }
  .corner-curve { position: absolute; top: 0; right: 0; }
  .brand {
    position: absolute;
    top: 50px; left: 0; width: 100%;
    display: flex; align-items: center; justify-content: center; gap: 12px;
  }
  .brand-dot {
    width: 54px; height: 54px; border-radius: 50%;
    border: 2px solid var(--green-dark);
  }
  .brand-name {
    font-family: "Cinzel", serif;
    font-weight: 500;
    color: var(--green-dark);
    line-height: 1;
  }
  .brand-name .line-1 { display: block; font-size: 40px; letter-spacing: 3px; }
  .brand-name .line-2 { display: block; font-size: 18px; letter-spacing: 2px; margin-top: 4px; }
  .wave-band { position: absolute; left: 0; top: 220px; }
  .photo-circle {
    position: absolute;
    width: 112px; height: 112px;
    border-radius: 50%;
    border: 4px solid var(--green-dark);
    outline: 2px solid var(--white);
    outline-offset: -6px;
  }
  .photo-1 { left: 31px;  top: 215px; background: linear-gradient(135deg, #e6d7c9, #7aa0c6); }
  .photo-2 { left: 166px; top: 242px; background: linear-gradient(135deg, #d8cfc6, #9db3c9); }
  .photo-3 { left: 298px; top: 242px; background: linear-gradient(135deg, #c8b9a8, #7d8590); }
  .photo-4 { left: 429px; top: 218px; background: linear-gradient(135deg, #c9c0a8, #4f8fc4); }
  .headline {
    position: absolute;
    top: 384px; left: 0; width: 100%;
    text-align: center;
    font-family: "Lora", serif;
    font-weight: 600;
    font-size: 23px;
    line-height: 24px;
    color: var(--green);
  }
  .services {
    position: absolute;
    top: 452px; left: 0; width: 100%;
    list-style: none;
    text-align: center;
    font-size: 15px;
    line-height: 26.6px;
    color: var(--text);
  }
  .services li::before { content: "• "; color: var(--green); }
  .footer {
    position: absolute;
    left: 0; bottom: 0;
    width: 100%; height: 64px;
    background: var(--green);
    color: var(--white);
    display: flex; align-items: center; justify-content: space-between;
    padding: 0 20px;
  }
  .address { font-size: 13px; font-weight: 600; line-height: 16px; }
  .address-right { text-align: right; }
  .phone { font-size: 22px; font-weight: 600; letter-spacing: 0.5px; }
</style>
</head>
<body>
  <main class="flyer">
    <div class="hero-photo" role="img" aria-label="Photo of a caregiver's hand gently holding an elderly person's hand"></div>

    <svg class="corner-curve" width="100" height="62" viewBox="0 0 100 62" aria-hidden="true">
      <path d="M0 0 H100 V62 C70 50 30 20 0 0 Z" fill="var(--green-dark)"/>
    </svg>

    <header class="brand">
      <span class="brand-dot" aria-hidden="true"></span>
      <h1 class="brand-name">
        <span class="line-1">WILLOWMERE</span>
        <span class="line-2">ELDER HOMES</span>
      </h1>
    </header>

    <svg class="wave-band" width="566" height="130" viewBox="0 0 566 130" aria-hidden="true">
      <path d="M0 20 C120 55 200 90 283 90 C370 90 470 50 566 15 V45 C470 80 370 118 283 118 C200 118 120 82 0 50 Z" fill="var(--green)"/>
    </svg>

    <div class="photo-circle photo-1" role="img" aria-label="Photo of a nurse chatting with a senior woman"></div>
    <div class="photo-circle photo-2" role="img" aria-label="Photo of a caregiver checking a resident's blood pressure"></div>
    <div class="photo-circle photo-3" role="img" aria-label="Photo of seniors laughing together at a table"></div>
    <div class="photo-circle photo-4" role="img" aria-label="Photo of a caregiver sharing a laugh with a senior woman"></div>

    <h2 class="headline">We provide the love and care needed to keep<br>your loved ones safely independent.</h2>

    <ul class="services">
      <li>24 Hours Care</li>
      <li>Assistance with Daily Living Activities</li>
      <li>Bathing Assistance</li>
      <li>Beauty and Haircare</li>
      <li>Laundry</li>
      <li>Linens</li>
      <li>Housekeeping</li>
      <li>3 Home-Cooked Meals and Snacks - Dietitian Approved</li>
      <li>Medication Reminders and Supervision</li>
      <li>Ambulatory Assistance and Supervision</li>
    </ul>

    <footer class="footer">
      <p class="address">212 Cypress Lane<br>Metairie, LA 70005</p>
      <p class="phone">(504) 555-0148</p>
      <p class="address address-right">4410 Magnolia Ct.<br>Metairie, LA 70002</p>
    </footer>
  </main>
</body>
</html>
```